Personal Business Card

Looking for a clean and modern personal business card. Basically I need something catchy to give to potential clients and people I meet. I do a lot of freelancing (from DJ'ing to wedding videography, but its mostly on the event side of things) so it's more-so about selling myself rather than identifying with a company. I'm starting to meet more people that I want to work with after meeting them so I'm revamping my business cards.

I'm looking for a clean and modern design- I know that's really vague but I'm fine with anything ranging from a symbol to just a fancy version of my name.

Details I need on the front:
Gerald Minsky
gerald@geraldminsky-demo.com
(555) 902-4416

On the back I'd like to have something simple like "Nice to have met you today" or "Great meeting you".

UPDATE 9/27 Noon: My apologies for not putting it up before- I'm definitely looking for full color. Doesn't have to be a rainbow but I am looking for the least amount of blank white as possible.

UPDATE 10/1: Really impressed with what I've been getting so far and I'm working on giving everyone feedback- if your design is still up then you're still in the run. Looking for something more unique and modern so please do not post something that looks like a template from Cardwell!

Target Market(s)

Mainly to give to people aged 18-35. Most of my encounters will be casual so the card should have a "young" feeling to it. I rarely do anything in the corporate world so it doesn't have to be boring. It should give the impression that I'm the one they should go to if they need what I do (again it changes every weekend so I'll probably say the "what I do" part.

Industry/Entity Type

Wedding

Requirements
Must have
• Basically the contact information listed above
Nice to have
• I really like the colors Blue, Silver, and Purple. They don't have to necessarily all be there though. I do like the look of polished metal if that makes sense.
Should not have
• A template that resembles card-well. I'm in a point in my life where I'm working a lot of different markets/areas so the card does not need to have an address or address placeholder.

```html
<!DOCTYPE html>
<html lang="en">
<head>
<meta charset="utf-8">
<title>Gerald Minsky – Business Card</title>
<link rel="stylesheet" href="https://fonts.googleapis.com/css2?family=Tangerine:wght@700&family=Tinos&display=swap">
<style>
  :root {
    --page-bg: #e9eaec;
    --card-white: #ffffff;
    --card-blue: #0a6bb5;
    --card-blue-mid: #4f9bd2;
    --script-ink: #7c7c98;
    --contact-ink: #111111;
    --card-shadow: rgba(20, 30, 50, 0.28);
  }
  * { margin: 0; padding: 0; box-sizing: border-box; }
  html, body {
    width: 1200px;
    height: 1200px;
    overflow: hidden;
    background: var(--page-bg);
  }
  .sheet {
    width: 1200px;
    height: 1200px;
    display: flex;
    flex-direction: column;
    align-items: center;
    justify-content: center;
    gap: 60px;
  }
  .card {
    position: relative;
    width: 900px;
    height: 514px;
    overflow: hidden;
    box-shadow: 0 14px 30px var(--card-shadow);
  }
  .card--back {
    background: linear-gradient(200deg, var(--card-white) 18%, var(--card-blue-mid) 62%, var(--card-blue) 100%);
  }
  .card--front {
    background: linear-gradient(70deg, var(--card-white) 8%, var(--card-blue-mid) 52%, var(--card-blue) 92%);
  }
  .greeting {
    position: absolute;
    left: 110px;
    bottom: 70px;
    font-family: "Tangerine", cursive;
    font-weight: 700;
    font-size: 128px;
    line-height: 1;
    color: var(--script-ink);
    transform: rotate(-6deg);
    transform-origin: left bottom;
  }
  .name {
    position: absolute;
    left: 300px;
    top: 40px;
    font-family: "Tangerine", cursive;
    font-weight: 700;
    font-size: 150px;
    line-height: 0.95;
    color: var(--script-ink);
  }
  .name__last {
    display: block;
    margin-left: -30px;
  }
  .contact {
    position: absolute;
    bottom: 64px;
    font-family: "Tinos", serif;
    font-size: 36px;
    color: var(--contact-ink);
  }
  .contact--phone { left: 36px; bottom: 150px; }
  .contact--email { right: 40px; }
</style>
</head>
<body>
  <main class="sheet">
    <section class="card card--back" aria-label="Card back">
      <p class="greeting">Nice meeting you</p>
    </section>
    <section class="card card--front" aria-label="Card front">
      <h1 class="name"><span class="name__first">Gerald</span><span class="name__last">Minsky</span></h1>
      <p class="contact contact--phone">(555) 902-4416</p>
      <p class="contact contact--email">gerald@geraldminsky-demo.com</p>
    </section>
  </main>
</body>
</html>
```